Willowmere Spa and Beauty Ltd. (Name of business)

I need a business card designed for this new company based out of Toronto Ontario. We specialize in Eyelash Extensions, Manicures and Pedicures, body waxing, massages, laser hair removal and botox treatments. Also offer a variety of products for sale, such as skin cream serums, collagen gel, eye cream, etc. It is a safe relaxing and non-judgemental environnment. Clients are welcome to come be pampered for the half or full day. Many service packages to choose from.

Open 7days per week from 8am to 8pm.

Priscilla Dunmore
Spa Facilitator
Willowmere Spa and Beauty Ltd.
7200 Harcourt St; Suite 1400
Toronto ON K2P 9W4

OFFICE: 416.790.4100
FAX: 416.790.4101
CELL: 416.632.1987
EMAIL: priscilla.dunmore@willowmerespa.com

Target Market(s)

Target market is primarily female ranging from 16 years old to 50 years old.

Industry/Entity Type

Business

Contact Information for Business Card

Priscilla Dunmore
Spa Facilitator
7200 Harcourt St; Suite 1400
Toronto ON K2P 9W4

OFFICE: 416.790.4100
FAX: 416.790.4101
CELL: 416.632.1987

Logo Text

I dont have a logo yet. I would like it simple but sophisticated and modern.

Font styles to use
Serif

Requirements
Must have
• all pertinent details such as company name, logo, name and contact information, services that are offered, including package rates
Nice to have
• Company name and logo prominent. A card that is neat and the information such as address, phone number, fax, email, etc is not too crowded but laid out in an easy to read format.
• Possibly on the back of card - some of the services offered could be listed, as well as professional cream lotions and serums. Hours of operation etc.

```html
<!DOCTYPE html>
<html lang="en">
<head>
<meta charset="utf-8">
<title>Willowmere Spa and Beauty – Business Card</title>
<link href="https://fonts.googleapis.com/css2?family=Tinos:wght@400;700&display=swap" rel="stylesheet">
<style>
  :root {
    --ink: #231f20;
    --band: #1f1c1c;
    --leaf: #7dc242;
    --leaf-light: #c8e03c;
    --paper: #ffffff;
    --frame: #2a2a2a;
  }
  * { margin: 0; padding: 0; box-sizing: border-box; }
  html, body { width: 1200px; height: 1000px; overflow: hidden; background: var(--paper); }
  body { position: relative; font-family: "Tinos", "Times New Roman", serif; font-weight: 700; color: var(--ink); }

  .card { position: absolute; left: 253px; width: 695px; height: 426px; border: 2px solid var(--frame); background: var(--paper); overflow: hidden; }
  .card--front { top: 67px; }
  .card--back { top: 507px; }

  /* front */
  .brand { position: absolute; top: 90px; left: 0; width: 100%; display: flex; justify-content: center; align-items: center; gap: 14px; }
  .brand__mark { width: 18px; height: 18px; border: 3px solid var(--ink); }
  .brand__name { font-size: 28px; letter-spacing: 0.3px; color: var(--ink); line-height: 1; }

  .rule { position: absolute; left: 0; top: 180px; width: 100%; height: 4px; background: var(--leaf); }
  .band { position: absolute; left: 0; top: 187px; width: 100%; bottom: 0; background: var(--band); color: var(--paper); }

  .details { position: absolute; left: 30px; top: 80px; font-size: 17px; line-height: 23px; }
  .details .city { margin-top: 3px; }

  .divider { position: absolute; left: 303px; top: 72px; width: 3px; height: 105px; background: var(--paper); }

  .contacts { position: absolute; left: 334px; top: 79px; list-style: none; font-size: 17px; }
  .contacts li { display: flex; align-items: center; height: 23px; }
  .contacts svg { width: 20px; height: 20px; flex: none; }
  .contacts .sep { color: var(--leaf); margin: 0 6px 0 6px; font-weight: 400; }
  .contacts .email { font-size: 16px; }

  /* back */
  .hours { position: absolute; left: 0; top: 0; width: 100%; height: 100%; }
  .hours__word { position: absolute; top: 156px; font-size: 33px; line-height: 1; }
  .hours__word--open { left: 181px; }
  .hours__word--days { left: 416px; }
  .hours__dial { position: absolute; left: 288px; top: 115px; width: 120px; height: 120px; }
  .hours__num { position: absolute; left: 288px; top: 122px; width: 120px; text-align: center; font-size: 96px; line-height: 1; font-style: italic; font-weight: 700; }
  .hours__week { position: absolute; left: 0; width: 100%; top: 238px; text-align: center; font-size: 25px; word-spacing: 4px; }
  .hours__time { position: absolute; left: 0; width: 100%; top: 283px; text-align: center; font-size: 25px; }
</style>
</head>
<body>

<section class="card card--front">
  <div class="brand">
    <span class="brand__mark"></span>
    <span class="brand__name">PRISCILLA DUNMORE</span>
  </div>
  <div class="rule"></div>
  <div class="band">
    <div class="details">
      <div>Spa Facilitator</div>
      <div>Willowmere Spa and Beauty Ltd.</div>
      <div>7200 Harcourt St; Suite 1400</div>
      <div class="city">Toronto ON K2P 9W4</div>
    </div>
    <div class="divider"></div>
    <ul class="contacts">
      <li>
        <svg viewBox="0 0 20 20" aria-label="Office"><circle cx="10" cy="10" r="8.5" fill="none" stroke="var(--leaf)" stroke-width="1.6"/><path d="M7 5.5c-1 .5-1.5 1.5-1 3 1 2.8 3 4.8 5.8 5.8 1.4.4 2.4 0 3-1l-1.8-1.8-1.4.8c-1.2-.6-2.2-1.6-2.8-2.8l.8-1.4z" fill="var(--leaf)"/></svg>
        <span class="sep">:</span>416.790.4100
      </li>
      <li>
        <svg viewBox="0 0 20 20" aria-label="Fax"><rect x="5" y="3" width="10" height="5" fill="none" stroke="var(--leaf)" stroke-width="1.5"/><rect x="2" y="8" width="16" height="8" rx="1.5" fill="var(--leaf)"/><rect x="6" y="11" width="8" height="2" fill="var(--band)"/></svg>
        <span class="sep">:</span>416.790.4101
      </li>
      <li>
        <svg viewBox="0 0 20 20" aria-label="Cell"><rect x="6.5" y="3" width="7" height="14" rx="1.2" fill="none" stroke="var(--leaf)" stroke-width="1.5"/><rect x="8" y="5" width="4" height="4" fill="var(--leaf)"/><circle cx="10" cy="14" r="1" fill="var(--leaf)"/></svg>
        <span class="sep">:</span>416.632.1987
      </li>
      <li>
        <svg viewBox="0 0 20 20" aria-label="Email"><rect x="2" y="5" width="16" height="11" fill="var(--leaf)"/><path d="M2 5l8 6 8-6" fill="none" stroke="var(--band)" stroke-width="1.4"/></svg>
        <span class="sep">:</span><span class="email">priscilla.dunmore@willowmerespa.com</span>
      </li>
    </ul>
  </div>
</section>

<section class="card card--back">
  <div class="hours">
    <span class="hours__word hours__word--open">OPEN</span>
    <svg class="hours__dial" viewBox="0 0 120 120" aria-hidden="true">
      <defs>
        <linearGradient id="dialGrad" x1="0" y1="0" x2="1" y2="1">
          <stop offset="0" stop-color="var(--leaf-light)"/>
          <stop offset="0.5" stop-color="var(--leaf)"/>
          <stop offset="1" stop-color="var(--leaf)"/>
        </linearGradient>
      </defs>
      <path d="M40 18 A52 52 0 1 0 66 8" fill="none" stroke="url(#dialGrad)" stroke-width="6"/>
      <path d="M28 13 L44 9 L40 25 Z" fill="var(--leaf)"/>
    </svg>
    <span class="hours__num">7</span>
    <span class="hours__word hours__word--days">DAYS</span>
    <div class="hours__week">PER WEEK</div>
    <div class="hours__time">FROM 8AM TO 8PM.</div>
  </div>
</section>

</body>
</html>
```